Ridgeline Build Network Inc. Letterhead

Creation of attractive and eye catching letterhead for a business start-up for the construction industry. Letterhead must relate to construction, but avoid standard hammer and tools in the design.
Updates

I forgot to add some details, sorry about that. Some pertinent info: Ph: 916-555-0148 ridgelinebuildnet.example 487 Willowmere Ave, Ste 210 Folsom, CA 95699 info@ridgelinebuildnet.example not sure if slogan should be in there" “Connecting construction professionals to create a purpose driven industry.” must be able to be used in word. Thanks!

```html
<!DOCTYPE html>
<html lang="en">
<head>
<meta charset="utf-8">
<title>Ridgeline Build Network Inc. Letterhead</title>
<link href="https://fonts.googleapis.com/css2?family=Open+Sans:wght@400;600;700&display=swap" rel="stylesheet">
<style>
  :root {
    --navy: #121b52;
    --red: #c0121a;
    --ink: #3d3d3d;
    --greeting: #2c2a5c;
    --paper: #ffffff;
    --backdrop: #e4e5e6;
  }
  * { box-sizing: border-box; margin: 0; padding: 0; }
  html, body { width: 1200px; height: 945px; overflow: hidden; background: var(--backdrop); }
  body { font-family: "Open Sans", Arial, sans-serif; color: var(--ink); }

  .letterhead {
    position: absolute; left: 280px; top: 20px;
    width: 640px; height: 905px;
    background: var(--paper);
    box-shadow: 0 2px 10px rgba(0,0,0,0.12);
    overflow: hidden;
  }
  .edge-band { position: absolute; left: 0; top: 0; width: 16px; height: 905px; }

  .brand-name {
    position: absolute; left: 52px; top: 44px;
    display: flex; align-items: center; gap: 8px;
    font-weight: 700; font-size: 15px; color: var(--navy); letter-spacing: 0.3px;
  }
  .brand-name .mark { width: 12px; height: 12px; background: var(--red); }

  .sender-address {
    position: absolute; right: 44px; top: 40px;
    font-size: 8.5px; line-height: 1.35; text-align: left;
  }
  .sender-address .company { color: var(--red); font-weight: 700; font-size: 9px; }

  .letter-body { position: absolute; left: 92px; top: 170px; width: 450px; }
  .greeting { font-weight: 700; font-size: 14px; color: var(--greeting); margin-bottom: 10px; }
  .letter-body p { font-size: 11px; line-height: 1.45; margin-bottom: 18px; text-align: justify; }

  .signature {
    position: absolute; left: 126px; top: 530px;
    width: 140px; height: 48px;
    background: linear-gradient(90deg, #f2f2f2, #e6e6e6);
    border-radius: 4px;
  }

  .corner-name {
    position: absolute; right: 48px; top: 726px;
    display: flex; align-items: center; gap: 6px;
    font-weight: 700; font-size: 10px; color: var(--navy);
  }
  .corner-name .mark { width: 9px; height: 9px; background: var(--red); }

  .contact-list {
    position: absolute; left: 92px; bottom: 36px;
    list-style: none; font-size: 9.5px; line-height: 1.5;
  }
  .contact-list li { display: flex; align-items: center; gap: 6px; }
  .contact-list svg { width: 9px; height: 9px; fill: var(--navy); }
</style>
</head>
<body>
<main class="letterhead">
  <svg class="edge-band" viewBox="0 0 16 905" preserveAspectRatio="none" aria-hidden="true">
    <rect x="0" y="0" width="16" height="660" fill="var(--navy)"/>
    <g stroke="var(--red)" stroke-width="3">
      <line x1="0" y1="672" x2="16" y2="662"/>
      <line x1="0" y1="680" x2="16" y2="670"/>
      <line x1="0" y1="688" x2="16" y2="678"/>
    </g>
    <rect x="0" y="694" width="16" height="211" fill="var(--red)"/>
  </svg>

  <div class="brand-name"><span class="mark"></span>Ridgeline Build Network Inc.</div>

  <address class="sender-address" style="font-style:normal">
    <div class="company">Ridgeline Build Network Inc.</div>
    <div>487 Willowmere Ave, Ste 210,</div>
    <div>Folsom, CA 95699</div>
  </address>

  <section class="letter-body">
    <div class="greeting">Dear Mr. Halvorsen,</div>
    <p>Lorem Ipsum is simply dummy text of the printing and typesetting industry. Lorem Ipsum has been the industry's standard dummy text ever since the 1500s, when an unknown printer took a galley of type and scrambled it to make a type specimen book. It has survived not only five centuries, but also the leap into electronic typesetting, remaining essentially unchanged.</p>
    <p>The standard chunk of Lorem Ipsum used since the 1500s is reproduced below for those interested. Sections 1.10.32 and 1.10.33 from "de Finibus Bonorum et Malorum" by Cicero are also reproduced in their exact original form, accompanied by English versions from the 1914 translation by H. Rackham</p>
    <p>Lorem Ipsum is simply dummy text of the printing and typesetting industry. Lorem Ipsum has been the industry's standard dummy text ever since the 1500s, when an unknown printer took a galley of type and scrambled it to make a type specimen book. It has survived not only five centuries, but also the leap into electronic typesetting, remaining essentially unchanged. It was popularised in the</p>
  </section>

  <div class="signature" role="img" aria-label="Handwritten signature of the sender"></div>

  <div class="corner-name"><span class="mark"></span>Ridgeline Build Network Inc.</div>

  <ul class="contact-list">
    <li><svg viewBox="0 0 10 10"><path d="M2 0.5 L3.6 2.6 L2.7 3.6 Q4 6.2 6.4 7.3 L7.4 6.4 L9.5 8 L8.3 9.5 Q1 8 0.5 1.7 Z"/></svg>916-555-0148</li>
    <li><svg viewBox="0 0 10 10"><path d="M0 2 H10 V8.5 H0 Z M0.8 2.6 L5 5.6 L9.2 2.6" fill="none" stroke="var(--navy)" stroke-width="1"/></svg>info@ridgelinebuildnet.example</li>
    <li><svg viewBox="0 0 10 10"><circle cx="5" cy="5" r="4.3" fill="none" stroke="var(--navy)" stroke-width="1"/><path d="M0.7 5 H9.3 M5 0.7 Q2.5 5 5 9.3 M5 0.7 Q7.5 5 5 9.3" fill="none" stroke="var(--navy)" stroke-width="0.8"/></svg>ridgelinebuildnet.example</li>
  </ul>
</main>
</body>
</html>
```